Business Card Design for Property Development Company Director

I am looking for a professional and unforgettable business card design for our Director of our Property Development Company.
Please see attached .pptx file to find out what information to include. You don't have to follow the exact format shown in the file - I am interested to see your creative flair using the information provided.

```html
<!DOCTYPE html>
<html lang="en">
<head>
<meta charset="utf-8">
<title>Kestmoor Property Group – Business Card</title>
<link rel="stylesheet" href="https://fonts.googleapis.com/css2?family=Lato:ital,wght@0,400;0,700;0,900;1,400&display=swap">
<style>
  :root {
    --brand-blue: #0b57a8;
    --brand-blue-deep: #094a90;
    --ink-grey: #555a60;
    --strip-grey: #5f6266;
    --card-white: #fbf8f7;
    --backdrop: #d9dadb;
  }
  * { box-sizing: border-box; margin: 0; padding: 0; }
  html, body { width: 1200px; height: 782px; overflow: hidden; }
  body {
    background: var(--backdrop);
    font-family: "Lato", sans-serif;
    position: relative;
  }
  .card {
    position: absolute;
    top: 233px;
    width: 520px;
    height: 316px;
    overflow: hidden;
    box-shadow: 0 10px 24px rgba(0,0,0,0.22);
  }
  /* Front */
  .card-front { left: 53px; background: var(--card-white); }
  .brand {
    position: absolute; left: 40px; top: 112px;
    display: flex; align-items: center; gap: 12px;
  }
  .brand-square { width: 40px; height: 40px; background: var(--brand-blue); }
  .brand-name {
    color: var(--brand-blue); font-weight: 900; font-size: 26px;
    letter-spacing: 0.5px; line-height: 1;
  }
  .brand-name small {
    display: block; font-size: 11px; font-weight: 900;
    letter-spacing: 3.2px; margin-top: 4px;
  }
  .divider {
    position: absolute; left: 268px; top: 62px; width: 1px; height: 150px;
    background: linear-gradient(to bottom, transparent, #b9bcc0 30%, #b9bcc0 70%, transparent);
  }
  .person { position: absolute; left: 292px; top: 84px; }
  .person-name { color: var(--brand-blue); font-weight: 900; font-size: 19px; letter-spacing: 0.3px; }
  .person-role { color: var(--ink-grey); font-size: 14px; margin-top: -2px; }
  .contact { list-style: none; margin-top: 20px; color: var(--ink-grey); font-size: 15px; }
  .contact li { display: flex; align-items: center; gap: 8px; line-height: 21px; }
  .contact svg { width: 12px; height: 12px; fill: var(--brand-blue); flex: none; }
  .licence-band {
    position: absolute; left: 0; bottom: 34px; width: 300px; height: 40px;
    background: var(--brand-blue);
    clip-path: polygon(0 0, 100% 0, 90% 100%, 0 100%);
    color: #fff; font-size: 12.5px; letter-spacing: 0.3px;
    display: flex; align-items: center; padding-left: 16px;
  }
  .grey-strip {
    position: absolute; left: 0; right: 0; bottom: 0; height: 34px;
    background: var(--strip-grey);
    clip-path: polygon(0 0, 55% 0, 52% 100%, 0 100%);
  }
  /* Back */
  .card-back { left: 627px; background: var(--brand-blue); }
  .pattern-field {
    position: absolute; inset: 0;
    background: linear-gradient(135deg, var(--brand-blue) 0%, var(--brand-blue-deep) 100%);
  }
  .tagline {
    position: absolute; right: 150px; bottom: 66px;
    color: #fff; text-align: right; font-size: 12.5px; line-height: 17px; letter-spacing: 0.2px;
    white-space: nowrap;
  }
  .tagline em { font-style: italic; }
  .back-brand {
    position: absolute; right: 28px; bottom: 94px;
    color: #fff; font-weight: 900; font-size: 18px; letter-spacing: 0.5px;
  }
</style>
</head>
<body>
  <section class="card card-front" aria-label="Business card front">
    <div class="brand">
      <span class="brand-square"></span>
      <div class="brand-name">KESTMOOR<small>PROPERTY GROUP</small></div>
    </div>
    <div class="divider"></div>
    <div class="person">
      <div class="person-name">DANIEL ASHFORD</div>
      <div class="person-role">Director</div>
      <ul class="contact">
        <li><svg viewBox="0 0 24 24"><path d="M6.6 10.8a15.1 15.1 0 0 0 6.6 6.6l2.2-2.2a1 1 0 0 1 1-.25 11.4 11.4 0 0 0 3.6.57 1 1 0 0 1 1 1V20a1 1 0 0 1-1 1A17 17 0 0 1 3 4a1 1 0 0 1 1-1h3.5a1 1 0 0 1 1 1c0 1.250.2 2.450.57 3.570a1 1 0 0 1-.25 1z"/></svg>0412 360 218</li>
        <li><svg viewBox="0 0 24 24"><path d="M2 5h20v14H2zm2 2v.5l8 5 8-5V7z"/></svg>daniel@kestmoor.com.au</li>
        <li><svg viewBox="0 0 24 24"><circle cx="12" cy="12" r="10"/></svg>www.kestmoor.com.au</li>
      </ul>
    </div>
    <div class="grey-strip"></div>
    <div class="licence-band">Real Estate Lic:&nbsp; 4172905 &amp; 4172906</div>
  </section>

  <section class="card card-back" aria-label="Business card back">
    <div class="pattern-field" role="img" aria-label="Faint repeating brand pattern on blue"></div>
    <p class="tagline">PROPERTY DEVELOPMENT<br>&amp; SITE ACQUISITION SPECIALISTS<br><em>Ask me about our</em> INVESTMENT &amp; PARTNERSHIP <em>opportunities</em></p>
    <div class="back-brand">KESTMOOR</div>
  </section>
</body>
</html>
```